Kelvoran belly band - cardboard to wrap around a plain tin for Gift

We are packaging men's and ladies handkerchiefs into tins for Gifts. We need two belly band designs to wrap around a small tin which measures 140 x 100 x 43 depth. The band to measure approx 90 w x 330 long inclusive is 30mm lapover . The ladies design (white tin) to have a subtle floral background with the word .Kelvoran. only placed on front centre of tin. The men's (black tin) to have a masculine look with the logo .Kelvoran. (the word can be taken out of the oval logo. This to placed in centre on front of tin. Men's could have a tan or cream textured look??

Target Market(s)

30 to 80 year old market

Font styles to use
Other font styles liked:
• Mona lisa

Colors

Designer to choose colors to be used in the design.

Requirements
Must have
• Two different designs one for men's black tin and one for ladies white tin.
• Must have continuous design with logo in centre once wrapped around the tin.
• Both must have an upmarket classy look.
• Tins will be displayed horizontal.
Nice to have
• Ladies would like to see soft floral not too over the top feminine classy look.
• Mens more masculine and upmarket maybe plain with a textured look.
• A design has been attached - like this sort of look for ladies!

```html
<!DOCTYPE html>
<html lang="en">
<head>
<meta charset="UTF-8">
<title>Kelvoran Belly Bands</title>
<link rel="stylesheet" href="https://fonts.googleapis.com/css2?family=Federo&display=swap">
<style>
  :root {
    --page: #ffffff;
    --cream: #efe1b9;
    --cream-deep: #e3d2a6;
    --cream-light: #f4e8c6;
    --cream-line: #2f2c28;
    --ink: #2e2b27;
    --plum-top: #b45ea7;
    --plum-mid: #d58fcc;
    --plum-bottom: #efc3e3;
    --plum-shade: rgba(170, 80, 160, 0.35);
    --plum-glow: rgba(245, 200, 235, 0.35);
    --gold: #f0b983;
  }
  * { margin: 0; padding: 0; box-sizing: border-box; }
  html, body {
    width: 1200px;
    height: 1138px;
    overflow: hidden;
    background: var(--page);
  }
  .canvas {
    position: relative;
    width: 1200px;
    height: 1138px;
  }
  .band {
    position: absolute;
    top: 56px;
    width: 278px;
    height: 1019px;
    display: flex;
    align-items: center;
    justify-content: center;
    overflow: hidden;
  }
  .band--mens {
    left: 64px;
    background: var(--cream);
  }
  .band--ladies {
    left: 858px;
    background: linear-gradient(180deg, var(--plum-top) 0%, var(--plum-mid) 55%, var(--plum-bottom) 100%);
  }
  .band__pattern {
    position: absolute;
    inset: 0;
  }
  .band--mens .band__pattern {
    background:
      linear-gradient(90deg, transparent 0%, var(--cream-deep) 18%, transparent 30%, var(--cream-light) 46%, transparent 58%, var(--cream-deep) 74%, transparent 88%),
      linear-gradient(180deg, var(--cream-light) 0%, transparent 20%, var(--cream-deep) 38%, transparent 55%, var(--cream-light) 72%, transparent 86%, var(--cream-deep) 100%);
    opacity: 0.55;
  }
  .band--ladies .band__pattern {
    background:
      radial-gradient(ellipse 120px 180px at 30% 12%, var(--plum-glow), transparent 70%),
      radial-gradient(ellipse 110px 160px at 75% 30%, var(--plum-glow), transparent 70%),
      radial-gradient(ellipse 120px 170px at 25% 48%, var(--plum-glow), transparent 70%),
      radial-gradient(ellipse 120px 180px at 35% 78%, var(--plum-shade), transparent 70%),
      radial-gradient(ellipse 110px 170px at 75% 90%, var(--plum-shade), transparent 70%),
      radial-gradient(ellipse 100px 150px at 78% 66%, var(--plum-shade), transparent 70%);
  }
  .band__rule {
    position: absolute;
    top: 0;
    bottom: 0;
    width: 1px;
  }
  .band--mens .band__rule { background: var(--cream-line); }
  .band--ladies .band__rule { background: var(--gold); }
  .band__rule--left { left: 13px; }
  .band__rule--right { right: 13px; }
  .wordmark {
    position: relative;
    display: flex;
    align-items: center;
    gap: 12px;
    font-family: "Federo", sans-serif;
    font-size: 50px;
    line-height: 1;
    letter-spacing: -1px;
    margin-top: 6px;
  }
  .wordmark__dot {
    width: 6px;
    height: 6px;
    border-radius: 50%;
    background: currentColor;
    margin-top: 4px;
  }
  .band--mens .wordmark { color: var(--ink); }
  .band--ladies .wordmark { color: var(--gold); }
</style>
</head>
<body>
<main class="canvas">
  <section class="band band--mens" aria-label="Men's belly band">
    <div class="band__pattern" role="img" aria-label="Subtle cream crosshatch linen texture"></div>
    <span class="band__rule band__rule--left"></span>
    <span class="band__rule band__rule--right"></span>
    <div class="wordmark"><span class="wordmark__dot"></span><span>Kelvoran</span><span class="wordmark__dot"></span></div>
  </section>

  <section class="band band--ladies" aria-label="Ladies' belly band">
    <div class="band__pattern" role="img" aria-label="Soft floral pattern of leaf and berry sprigs in tonal pink"></div>
    <span class="band__rule band__rule--left"></span>
    <span class="band__rule band__rule--right"></span>
    <div class="wordmark"><span class="wordmark__dot"></span><span>Kelvoran</span><span class="wordmark__dot"></span></div>
  </section>
</main>
</body>
</html>
```